Revamp Zelvaro Inc website

A complete revamp of the www.zelvaro-app.com website.
Strong actionable landing pages.
An in-house site was being done but was abandoned. See http://www.pagebuildr-demo.com/tovrin/zelvaro and once in, click on the "Home" to go to the main Home page.
Updates

A new YouTube Standard Video has just been posted: http://www.clipvessa-demo.com/watch?v=Q-7mk2LpWzA&feature=email

I thought that I would share what was being done in-house, but was abandoned.

Once launched you will come to the main landing page, then click on the "Home" button to see the main home page. I thought this was rather interesting. One problem here is Flash, most smartphones don't support Flash and our market is in that world, so Flash really is not a good option.

Project Deadline Extended
Reason: Please can you submit one more design, we have a dead tie with voting.

Project Deadline Extended
Reason: Request as per a designer.

Target Market(s)

Zelvaro for all intense purposes is mobile Drivgard on steroids. Currently running on Android, BB and iPhone. End of Jan 2012 we will run on ANY J2ME (Java) supported phone as well. Here we will be talking directly to the OBD (onboard diagnostics) in the car. In the event of the car's airbags being deployed emergency services, ES, (whether public, 911 or other country equivalent, or private, alarm company) the application will not only call the ES but also log the gps information. Other services include: SOS, Nurse Lines, Roadside, Notify Friends and Family.
Zelvaro determines the ERC by the phones location, thus assuming not private in the USA will reach out to 911, Europe 112 etc.

Zelvaro is about making a pro and re active emergency solution to the masses. It must be affordable to anyone owning a cell phone (thus: 9 cents per day). The emphasis is on the person not the asset as Drivgard and other competitors are. It must be adaptable to ones environment

Zelvaro target market sale is a top-down (Corporate to consumer) we do offer:
* white-labeling (see www.brennholt-mobile-demo.com) as well as non branded solutions (Zelvaro branded),
* private emergency response center call and data routing - here the emergency call is routed the the companies emergency call center (example: alarm company, security firm, campus police), and the location and user details data details on file are pushed as well.

As such our target corporate market primarily is:
Security, Home Alarm, Insurance, University Campus Police, Auto, Smartphone users, Roadside assistance

Our ultimate target audience is cell phone users, where security, safety and peace of mind of oneself, family and/or team members is of importance.

Industry/Entity Type

House

Requirements
Must have
• Must have strong actionable call to action features
Must have multiple actionable landing pages
Must link to our ecommerce
Must link into blog
Must be able to cellphone friendly (i.e.: no flash)
Must be SEO

```html
<!DOCTYPE html>
<html lang="en">
<head>
<meta charset="utf-8">
<title>Zelvaro Inc</title>
<link href="https://fonts.googleapis.com/css2?family=Open+Sans:wght@400;600&display=swap" rel="stylesheet">
<style>
:root{
  --bg-top:#e4e4e4;
  --bg-mid:#ededed;
  --bg-bottom:#d6d6d6;
  --ink:#555;
  --ink-soft:#888;
  --ink-heading:#444;
  --logo:#6a6a6a;
  --card:#f6f5f5;
  --card-edge:#ffffff;
  --nav-top:#e9e9e9;
  --nav-bottom:#c9c9c9;
  --pill:#8a8a8a;
  --rule:#c2c2c2;
  --badge:#3a3a3a;
}
*{margin:0;padding:0;box-sizing:border-box}
html,body{width:1200px;height:1090px;overflow:hidden}
body{
  position:relative;
  font-family:"Open Sans",Arial,sans-serif;
  color:var(--ink);
  background:linear-gradient(180deg,var(--bg-top) 0,var(--bg-mid) 280px,var(--bg-bottom) 1090px);
}
.logo{position:absolute;left:175px;top:28px;font-size:40px;color:var(--logo);letter-spacing:1px;font-weight:400}
.nav{
  position:absolute;left:553px;top:22px;width:472px;height:51px;border-radius:6px;
  background:linear-gradient(180deg,var(--nav-top),var(--nav-bottom));
  border:1px solid #bdbdbd;box-shadow:0 2px 4px rgba(0,0,0,.15);
  display:flex;align-items:center;padding-left:16px;gap:0;
}
.nav a{font-size:13px;color:#666;text-decoration:none;padding:3px 15px;margin-right:8px;border-radius:4px}
.nav a.active{background:var(--pill);color:#fff;box-shadow:inset 0 1px 2px rgba(0,0,0,.3)}
.callout{
  position:absolute;width:267px;height:91px;border-radius:6px;background:var(--card);
  border:1px solid var(--card-edge);box-shadow:0 2px 5px rgba(0,0,0,.12);
}
.callout .icon{position:absolute;top:14px;width:64px;height:62px;border-radius:12px}
.callout .copy{position:absolute;top:14px;font-size:12px;line-height:18px;color:#777}
.callout .copy h3{font-size:13px;font-weight:400;color:#555;margin-bottom:6px}
.callout.left .icon{left:10px}
.callout.left .copy{left:91px}
.callout.right .icon{right:12px}
.callout.right .copy{right:92px;transform:scaleX(-1);text-align:left}
.arrows{position:absolute;left:0;top:0}
.phone{
  position:absolute;left:455px;top:103px;width:255px;height:495px;border-radius:52px;
  background:linear-gradient(160deg,#3a3a3a,#0c0c0c 55%,#222);
  border:3px solid #9a9a9a;box-shadow:0 40px 40px -20px rgba(0,0,0,.35);
}
.phone .screen{
  position:absolute;left:14px;top:80px;width:221px;height:334px;
  background:linear-gradient(180deg,#dfe7ef,#1f57a6 40%,#0c3f86);
}
.phone .home-key{position:absolute;left:103px;top:428px;width:44px;height:44px;border-radius:50%;border:2px solid #444}
.phone .speaker{position:absolute;left:100px;top:42px;width:52px;height:6px;border-radius:3px;background:#555}
h2{position:absolute;left:179px;font-size:29px;font-weight:400;color:var(--ink-heading);letter-spacing:-.5px}
.rule{position:absolute;left:395px;width:630px;height:1px;background:var(--rule);box-shadow:0 1px 0 #f2f2f2}
.about-text{position:absolute;left:180px;top:683px;width:815px;font-size:12.5px;line-height:18px;color:var(--ink-soft)}
.features{position:absolute;top:846px;list-style:none;font-size:12.5px;color:var(--ink-soft)}
.features li{height:25px;padding-left:21px;position:relative}
.features li svg{position:absolute;left:0;top:-4px}
.stores{position:absolute;top:983px;height:49px;width:174px;border-radius:2px;background:var(--badge);border-bottom:2px solid #222}
.footer-rule{position:absolute;left:240px;top:1052px;width:740px;height:1px;background:linear-gradient(90deg,transparent,#c4c4c4,transparent)}
.copyright{position:absolute;left:0;width:1256px;top:1061px;text-align:center;font-size:12px;color:#777}
</style>
</head>
<body>

<div class="logo">Zelvaro Inc</div>

<nav class="nav">
  <a class="active" href="#">Home</a>
  <a href="#">Features</a>
  <a href="#">Downloads</a>
  <a href="#">FAQ</a>
  <a href="#">Developments</a>
</nav>

<svg class="arrows" width="1200" height="600" aria-hidden="true">
  <g fill="#f6f5f5" stroke="#ffffff" stroke-width="1">
    <polygon points="380,206 410,206 410,178 475,225 410,271 410,246 380,246"/>
    <polygon points="380,326 410,326 410,298 475,345 410,391 410,366 380,366"/>
    <polygon points="380,446 410,446 410,418 475,465 410,511 410,486 380,486"/>
    <polygon points="790,206 760,206 760,178 695,225 760,271 760,246 790,246"/>
    <polygon points="790,326 760,326 760,298 695,345 760,391 760,366 790,366"/>
    <polygon points="790,446 760,446 760,418 695,465 760,511 760,486 790,486"/>
  </g>
</svg>

<div class="callout left" style="left:115px;top:180px">
  <div class="icon" role="img" aria-label="Lifebuoy icon" style="background:radial-gradient(circle,#f3f3f3 30%,#e2622a 32%,#f0f0f0 70%)"></div>
  <div class="copy"><h3>Lorem Ipsum Dolor Amet.</h3>Lorem ipsum dolor sit amet,<br>consectetur adipiscing elit.</div>
</div>
<div class="callout left" style="left:115px;top:300px">
  <div class="icon" role="img" aria-label="Blue flag icon" style="background:linear-gradient(135deg,#9cc7f0,#5f9ad6)"></div>
  <div class="copy"><h3>Lorem Ipsum Dolor Amet.</h3>Lorem ipsum dolor sit amet,<br>consectetur adipiscing elit.</div>
</div>
<div class="callout left" style="left:115px;top:420px">
  <div class="icon" role="img" aria-label="User silhouette icon" style="background:linear-gradient(180deg,#555,#222)"></div>
  <div class="copy"><h3>Lorem Ipsum Dolor Amet.</h3>Lorem ipsum dolor sit amet,<br>consectetur adipiscing elit.</div>
</div>

<div class="callout right" style="left:787px;top:180px">
  <div class="icon" role="img" aria-label="Clock icon" style="background:radial-gradient(circle,#ffffff 55%,#7fa6d9 58%,#c8d8ee 75%)"></div>
  <div class="copy"><h3>Lorem Ipsum Dolor Amet.</h3>Lorem ipsum dolor sit amet,<br>consectetur adipiscing elit.</div>
</div>
<div class="callout right" style="left:787px;top:300px">
  <div class="icon" role="img" aria-label="Orange heart icon" style="background:linear-gradient(180deg,#f07a2c,#d35612)"></div>
  <div class="copy"><h3>Lorem Ipsum Dolor Amet.</h3>Lorem ipsum dolor sit amet,<br>consectetur adipiscing elit.</div>
</div>
<div class="callout right" style="left:787px;top:420px">
  <div class="icon" role="img" aria-label="Settings gear icon" style="background:radial-gradient(circle,#e6ecec 20%,#a9b6b6 22%,#cfd8d8 70%)"></div>
  <div class="copy"><h3>Lorem Ipsum Dolor Amet.</h3>Lorem ipsum dolor sit amet,<br>consectetur adipiscing elit.</div>
</div>

<div class="phone" role="img" aria-label="Smartphone showing the Zelvaro app home screen with SOS, Notify, Repair and Nurse buttons">
  <div class="speaker"></div>
  <div class="screen"></div>
  <div class="home-key"></div>
</div>

<h2 style="top:630px">About The App</h2>
<div class="rule" style="top:653px"></div>
<p class="about-text">Lorem ipsum dolor sit amet, consectetur adipiscing elit. Cras in leo at sapien varius tristique. Ut dapibus sodales libero a malesuada. Aenean ullamcorper convallis lorem at hendrerit. Nam vel arcu lacus. Cras dapibus egestas mi in porttitor. Vestibulum massa metus, vestibulum non consectetur vel, congue ullamcorper sapien. Aenean semper aliquet leo, in posuere justo faucibus eget. Proin pulvinar risus libero, non ullamcorper nulla.</p>

<h2 style="top:795px">Features List</h2>
<div class="rule" style="top:818px"></div>

<ul class="features" style="left:178px">
  <li><svg width="12" height="12" viewBox="0 0 12 12"><path d="M1 6l3 3 7-8" fill="none" stroke="#777" stroke-width="2"/></svg>Lorem ipsum dolor sit amet, consectetur adipiscing.</li>
  <li><svg width="12" height="12" viewBox="0 0 12 12"><path d="M1 6l3 3 7-8" fill="none" stroke="#777" stroke-width="2"/></svg>Lorem ipsum dolor sit amet, consectetur adipiscing.</li>
  <li><svg width="12" height="12" viewBox="0 0 12 12"><path d="M1 6l3 3 7-8" fill="none" stroke="#777" stroke-width="2"/></svg>Lorem ipsum dolor sit amet, consectetur adipiscing.</li>
  <li><svg width="12" height="12" viewBox="0 0 12 12"><path d="M1 6l3 3 7-8" fill="none" stroke="#777" stroke-width="2"/></svg>Lorem ipsum dolor sit amet, consectetur adipiscing.</li>
</ul>
<ul class="features" style="left:608px">
  <li><svg width="12" height="12" viewBox="0 0 12 12"><path d="M1 6l3 3 7-8" fill="none" stroke="#777" stroke-width="2"/></svg>Lorem ipsum dolor sit amet, consectetur adipiscing.</li>
  <li><svg width="12" height="12" viewBox="0 0 12 12"><path d="M1 6l3 3 7-8" fill="none" stroke="#777" stroke-width="2"/></svg>Lorem ipsum dolor sit amet, consectetur adipiscing.</li>
  <li><svg width="12" height="12" viewBox="0 0 12 12"><path d="M1 6l3 3 7-8" fill="none" stroke="#777" stroke-width="2"/></svg>Lorem ipsum dolor sit amet, consectetur adipiscing.</li>
  <li><svg width="12" height="12" viewBox="0 0 12 12"><path d="M1 6l3 3 7-8" fill="none" stroke="#777" stroke-width="2"/></svg>Lorem ipsum dolor sit amet, consectetur adipiscing.</li>
</ul>

<div class="stores" style="left:340px;top:985px"></div>
<div class="stores" style="left:531px"></div>
<div class="stores" style="left:720px"></div>

<div class="footer-rule"></div>
<p class="copyright">Copyright Zelvaro, All Rights Reserved</p>

</body>
</html>
```